A5 Patient Information Booklet (Chiropractic Clinic) 4-8 pages

Here’s a polished, professional rewrite of your full brief and content, with clearer structure, corrected language, and a premium tone:

---

**Project Title:** Premium Patient Information Brochure (Chiropractic & Wellness Clinic)

---

### **Overview**

We are a health and wellness clinic seeking a premium, high-end patient information brochure to provide following a patient’s initial consultation and first treatment.

The purpose of this booklet is to:

* Reinforce trust and professionalism
* Help patients understand what to expect next
* Encourage adherence to care recommendations
* Position the clinic as calm, expert-led, and results-driven

---

### **Format**

* 4–8 page booklet (A5 or similar size)
* Print-ready and digital versions required

---

### **Target Audience**

Patients who have just completed their initial consultation and may have begun treatment. They may already be experiencing physical or mental changes, so the brochure should guide, reassure, and educate them on what comes next.

---

### **Tone & Style**

* Premium, calm, and reassuring
* Modern wellness aesthetic (not overly clinical)
* Clean layout with minimal clutter
* Soft, neutral colour palette (whites, creams, muted greens, soft blues)
* Elegant typography (e.g. Montserrat / Lato)
* High-end, trustworthy, and professional feel

---

### **Key Messages**

#### 1. Listen to Your Body

Patients may feel different after treatment. Reassure them that this is normal and part of the healing process.

#### 2. Post-Treatment Advice

* Stay well hydrated
* Rest if needed
* Avoid overexertion if the body requires recovery

#### 3. Healing is a Journey (Core Concept)

A strong visual metaphor of a **“road to recovery”** or **journey** should be central to the design.

This journey should clearly illustrate three phases:

* **Phase 1: Initial Care (Weeks 1–6)**
Focus: Reducing pain/discomfort, calming the body, and initiating response to treatment

* **Phase 2: Corrective Care (Weeks 6–12)**
Focus: Addressing underlying issues, improving function, and creating lasting change

* **Phase 3: Wellness / Maintenance (Ongoing)**
Focus: Maintaining progress, preventing relapse, and supporting long-term wellbeing

**Important:**

* Emphasise that this is not a quick fix
* Progress requires time and consistency
* Each patient follows an individualised care plan
* The journey should feel structured, positive, and achievable

#### 4. Personalised Care

Reinforce that every treatment plan is tailored specifically to the individual.

#### 5. Professional Reassurance

Patients should feel confident they are in expert hands and supported throughout their journey.

---

### **Design Direction**

* Use imagery that reflects calmness, progression, and wellness (e.g. pathways, nature, soft gradients)
* Avoid generic stock imagery
* **Only use original clinic images from website and social media**
* Prioritise white space and clarity
* Aim for a luxury spa/medical hybrid aesthetic

---

## **Content Structure (Page-by-Page)**

### **Front Cover**

* Clean, minimal, premium design
* Clinic branding

---

### **Page 1: Patient Case Summary**

**Title:** *Welcome to Larkmoor Spine Studio*

Thank you for choosing Larkmoor Spine Studio.

This booklet is designed to guide you through:

* What we found during your initial consultation
* Your personalised recommended treatment plan
* Your road to recovery
* Long-term wellness care
* Why we take the approach we do

---

### **Page 2: Your Care Journey**

**Stage 1: Your Initial Consultation**

Today we completed a comprehensive assessment of your health and function, including:

* Full case history and discussion of your symptoms and goals
* Orthopaedic and neurological testing
* Postural and movement assessment
* Initial treatment (where appropriate)

**What this tells us:**

* How your body is currently functioning
* Where areas of stress or dysfunction may be present
* The most appropriate and effective path forward for your care

---

### **Page 3: Your Suggested Treatment Plan**

Based on today’s findings, your recommended care plan is:

**______ treatments over ______ weeks**

This should be viewed alongside your *Road to Recovery* to help you understand what to expect.

We have also discussed:

* Expected timelines for improvement
* Available payment options

**After Treatment:**
It is common to feel different following treatment. This is a normal response as your body begins to adapt and respond.

We recommend:

* Staying well hydrated
* Allowing time for rest and recovery
* Avoiding overexertion if your body feels it needs it

---

### **Page 4: What to Expect Next**

Healing is not always linear—it is a process that occurs over time.

Your care will typically progress through the following stages:

* **Relief Care**
Focused on reducing discomfort and calming the body

* **Corrective Care**
Focused on addressing underlying issues and improving function
(This phase may include prescribed exercises)

* **Maintenance / Wellness Care**
Focused on sustaining progress, preventing recurrence, and supporting long-term health

---

### **Page 5: Understanding Chiropractic Care**

**What is Chiropractic?**
Chiropractic care focuses on the relationship between the spine, nervous system, and overall body function.

By improving spinal movement and alignment, chiropractic care helps support the nervous system, allowing the body to function and heal more effectively.

**About Larkmoor Spine Studio**
At Larkmoor Spine Studio, our approach is centred around personalised, patient-focused care. We aim to not only relieve symptoms but to address underlying causes and support long-term wellbeing.

---

### **Back Page**

* Clinic contact details
* Website
* Social media icons/handles

**Closing Message:**
“A healthier, stronger you—supported every step of the way.”

---

### **Deliverables**

* Print-ready PDF
* Editable source files

---

### **Additional Notes**

* The brochure should feel valuable and worth keeping
* Encourage long-term care in a subtle, non-pushy way
* Maintain clarity, readability, and strong visual hierarchy
* Balance professionalism with warmth and approachability

---

If you’d like, I can also turn this into **actual brochure copy (fully written, patient-facing text)** or help you refine it further for a designer.

Target Market(s)

Existing patients who want to feel better and look after themselves that is given after their initil consultation appointment

Industry/Entity Type

Chiropractic, wellness, health

Font styles to use
Other font styles liked:
• Montserrat or Lato

Colors
0094D4
00A9DD
6FCCEA
C7EBF8
E9F6FB
00AB8E
00BBA5
67D7C9
C6EFE9
E9F9F6
6B429C
8869AF
B7A5CE
E3DAEB
F3F0F8

Requirements
Must have
• my own photos, look premium wellness, be clear and simple to understand for patients journey or what to expect next and over time
Nice to have
• USe my social media/website for ideas
Should not have
• generic photos and images

```html
<!DOCTYPE html>
<html lang="en">
<head>
<meta charset="utf-8">
<title>Larkmoor Spine Studio – Patient Booklet Spreads</title>
<link href="https://fonts.googleapis.com/css2?family=Inter:wght@400;500;600;700&display=swap" rel="stylesheet">
<style>
  :root {
    --stage: #d1d1d1;
    --paper: #ffffff;
    --ink: #2c3e50;
    --body: #3a3f44;
    --teal: #00ab8e;
    --teal-bright: #00bba5;
    --teal-soft: #c6e6e1;
    --teal-tint: #e9f9f6;
    --blue: #0094d4;
    --blue-bright: #00a9dd;
    --blue-tint: #e9f6fb;
    --purple: #8869af;
    --purple-tint: #f3f0f8;
    --mist: #e4e5e7;
  }
  * { margin: 0; padding: 0; box-sizing: border-box; }
  html, body { width: 860px; height: 1200px; overflow: hidden; background: var(--stage); }
  body { position: relative; font-family: "Inter", sans-serif; color: var(--body); }

  .spread { position: absolute; left: 77px; width: 706px; height: 501px; background: var(--paper); overflow: hidden; }
  .spread--care { top: 79px; }
  .spread--journey { top: 619px; background: linear-gradient(180deg, #fff 0%, #fff 58%, #e6f4f2 75%, #c6e6e1 100%); }
  .abs { position: absolute; }

  .section-title { position: absolute; font-size: 16px; font-weight: 600; color: var(--ink); letter-spacing: -0.1px; white-space: nowrap; }
  .section-title .accent { color: var(--teal-bright); }
  .lede { position: absolute; font-size: 7.6px; line-height: 11px; color: var(--body); }

  /* care plan form */
  .plan-form { left: 30px; top: 91px; width: 292px; height: 118px; background: var(--teal-soft); border-radius: 4px; padding: 10px 11px 0; font-size: 7.6px; }
  .plan-form .row { height: 14.2px; display: flex; align-items: flex-end; white-space: nowrap; }
  .plan-form .line { flex: 1; border-bottom: 0.7px solid #4d5a60; margin-left: 2px; margin-bottom: 2px; }
  .plan-form .line--short { flex: 0 0 50px; margin-right: 3px; }
  .plan-form .note { position: absolute; left: 11px; bottom: 10px; font-size: 5.8px; font-weight: 500; }

  /* support features */
  .feature { position: absolute; display: flex; align-items: center; width: 150px; }
  .feature .badge { width: 30px; height: 30px; border-radius: 50%; background: var(--teal-soft); display: flex; align-items: center; justify-content: center; flex: none; margin-right: 11px; }
  .feature p { font-size: 7.6px; line-height: 10.6px; }

  .quote { left: 30px; width: 292px; top: 362px; text-align: center; font-size: 11.6px; font-weight: 500; line-height: 17px; color: var(--teal); }

  /* brand marks */
  .brand-dot { position: absolute; border-radius: 50%; border: 1.2px solid var(--teal-bright); }
  .brand-name { position: absolute; font-weight: 600; color: var(--ink); white-space: nowrap; text-align: center; }

  .contacts { left: 106px; top: 425px; font-size: 6.1px; line-height: 10.4px; color: var(--body); }
  .contacts li { list-style: none; display: flex; align-items: center; gap: 5px; }
  .contacts li.social { margin-top: 5px; }

  .cover-kicker { left: 383px; top: 131px; font-size: 16px; font-weight: 600; color: var(--teal-bright); }
  .cover-title { left: 382px; top: 150px; font-size: 33px; font-weight: 700; line-height: 37px; color: var(--ink); }
  .cover-tagline { left: 382px; top: 246px; font-size: 12.6px; font-weight: 500; line-height: 19.5px; color: var(--teal-bright); }
  .figure-art { left: 500px; top: 115px; width: 206px; height: 350px; border-radius: 90px 60px 40px 80px; background: linear-gradient(160deg, rgba(228,229,231,0.0) 0%, rgba(228,229,231,0.55) 45%, rgba(228,229,231,0.25) 100%); }

  /* expectations */
  .expect { position: absolute; top: 89px; display: flex; width: 200px; }
  .expect .badge { width: 34px; height: 34px; border-radius: 50%; flex: none; margin-right: 12px; margin-top: 2px; display: flex; align-items: center; justify-content: center; }
  .expect h3 { font-size: 10px; font-weight: 600; margin-bottom: 4px; }
  .expect p { font-size: 7.6px; line-height: 10.8px; }
  .expect--listen h3 { color: var(--blue-bright); } .expect--listen .badge { background: var(--blue-bright); }
  .expect--support h3 { color: var(--teal-bright); } .expect--support .badge { background: var(--teal-bright); }
  .expect--trust h3 { color: var(--purple); } .expect--trust .badge { background: var(--purple); }

  /* phases */
  .phase { position: absolute; top: 229px; width: 153px; height: 98px; border-radius: 4px; padding: 13px 16px 0; border: 0.8px solid; }
  .phase h3 { font-size: 10px; font-weight: 600; margin-bottom: 3px; }
  .phase .span { font-size: 7.6px; font-weight: 600; color: var(--ink); margin-bottom: 5px; }
  .phase p { font-size: 7.6px; line-height: 10.8px; }
  .phase--relief { left: 30px; background: linear-gradient(180deg, #d9f0fa 0%, #fff 45%); border-color: #c7ebf8; }
  .phase--relief h3 { color: var(--blue-bright); }
  .phase--corrective { left: 277px; background: linear-gradient(180deg, #d3efe9 0%, #fff 45%); border-color: #c6efe9; }
  .phase--corrective h3 { color: var(--teal-bright); }
  .phase--wellness { left: 524px; background: linear-gradient(180deg, #e8e1f0 0%, #fff 45%); border-color: #e3daeb; }
  .phase--wellness h3 { color: var(--purple); }
  .connector { position: absolute; top: 327px; height: 24px; border-left: 0.8px dashed #7fcfc6; }

  .road { left: 0; top: 340px; width: 706px; height: 120px; }
  .walker { left: 91px; top: 363px; width: 22px; height: 42px; border-radius: 10px; background: linear-gradient(180deg, #3a4a55, #2c3e50); }

  .promise { position: absolute; top: 462px; display: flex; align-items: center; gap: 4px; font-size: 8.6px; color: var(--ink); white-space: nowrap; }
</style>
</head>
<body>

<!-- Spread: care plan and cover -->
<section class="spread spread--care">
  <h2 class="section-title" style="left:30px;top:25px;"><span class="accent">Your Personalised</span> Care Plan</h2>
  <p class="lede" style="left:30px;top:53px;width:300px;">Your body is unique. Your plan should be too. We’ve created a care plan tailored to your needs and goals.</p>

  <div class="abs plan-form">
    <div class="row">Patient Name:<span class="line"></span></div>
    <div class="row">Your Suggested Care Plan:<span class="line"></span></div>
    <div class="row">Treatments over<span class="line line--short"></span>weeks</div>
    <div class="row">Notes:<span class="line"></span></div>
    <div class="row"><span class="line" style="margin-left:0"></span></div>
    <div class="row"><span class="line" style="margin-left:0"></span></div>
    <p class="note">*We will review your progress regularly and adjust your plan as you improve.</p>
  </div>

  <h2 class="section-title" style="left:30px;top:234px;"><span class="accent">We are here to</span> Support You</h2>

  <div class="feature" style="left:30px;top:268px;">
    <span class="badge"><svg width="16" height="16" viewBox="0 0 16 16" fill="none" stroke="#00ab8e" stroke-width="1"><path d="M8 13 3 8.2A2.6 2.6 0 0 1 8 5a2.6 2.6 0 0 1 5 3.2Z"/></svg></span>
    <p>Expert care from qualified professionals.</p>
  </div>
  <div class="feature" style="left:194px;top:268px;">
    <span class="badge"><svg width="16" height="16" viewBox="0 0 16 16" fill="none" stroke="#00ab8e" stroke-width="1"><rect x="3.5" y="2" width="9" height="12" rx="1"/><path d="M5.5 5.5h5M5.5 8h5M5.5 10.5h3"/></svg></span>
    <p>Personalised treatment just for you.</p>
  </div>
  <div class="feature" style="left:30px;top:309px;">
    <span class="badge"><svg width="16" height="16" viewBox="0 0 16 16" fill="none" stroke="#00ab8e" stroke-width="1"><path d="M3 13V9h2v4M7 13V7h2v6M11 13V4h2v9"/></svg></span>
    <p>Ongoing support at every stage.</p>
  </div>
  <div class="feature" style="left:194px;top:309px;">
    <span class="badge"><svg width="16" height="16" viewBox="0 0 16 16" fill="none" stroke="#00ab8e" stroke-width="1"><circle cx="8" cy="4.5" r="2"/><path d="M4 9c1 2 2.5 2.5 4 2.5S11 11 12 9M8 11.5V14"/></svg></span>
    <p>Helping you move, feel and live better.</p>
  </div>

  <p class="abs quote">“Your health is an investment in your future.<br>We’re here for the long run.”</p>

  <span class="brand-dot" style="left:45px;top:421px;width:34px;height:34px;"></span>
  <span class="brand-name" style="left:20px;top:459px;width:84px;font-size:6.6px;">Larkmoor Spine Studio</span>

  <ul class="abs contacts">
    <li><svg width="7" height="7" viewBox="0 0 10 10" fill="none" stroke="#2c3e50" stroke-width="1"><path d="M5 9.5S1.8 6 1.8 4a3.2 3.2 0 0 1 6.4 0C8.2 6 5 9.5 5 9.5Z"/><circle cx="5" cy="4" r="1.1"/></svg>12 Fernhill Row, Ashcombe, Somerset, AB1 2CD, United Kingdom</li>
    <li><svg width="7" height="7" viewBox="0 0 10 10" fill="none" stroke="#2c3e50" stroke-width="1"><rect x="1" y="2" width="8" height="6"/><path d="m1 2 4 3.5L9 2"/></svg>Email: hello@larkmoorspine.com</li>
    <li><svg width="7" height="7" viewBox="0 0 10 10" fill="none" stroke="#2c3e50" stroke-width="1"><circle cx="5" cy="5" r="4"/><path d="M1 5h8M5 1c-2 2.5-2 5.5 0 8M5 1c2 2.5 2 5.5 0 8"/></svg>Website: www.larkmoorspine.com</li>
    <li class="social">larkmoorspinestudio</li>
  </ul>

  <span class="brand-dot" style="left:400px;top:37px;width:42px;height:42px;"></span>
  <span class="brand-name" style="left:371px;top:83px;width:100px;font-size:7.4px;">Larkmoor Spine Studio</span>

  <div class="abs figure-art" role="img" aria-label="Faint line illustration of a human figure outline"></div>

  <p class="abs cover-kicker">Your Guide to</p>
  <h1 class="abs cover-title">Healing &amp;<br>Wellness</h1>
  <p class="abs cover-tagline">Personalised Care.<br>Real Results. Lasting Change.</p>
</section>

<!-- Spread: what to expect and recovery journey -->
<section class="spread spread--journey">
  <h2 class="section-title" style="left:30px;top:28px;"><span class="accent">What to Expect</span> After Your Treatment</h2>
  <p class="lede" style="left:30px;top:57px;">It’s normal to feel different after your adjustment. Your body is responding and beginning to heal.</p>

  <div class="expect expect--listen" style="left:30px;">
    <span class="badge"><svg width="18" height="18" viewBox="0 0 18 18" fill="none" stroke="#fff" stroke-width="1.1"><circle cx="9" cy="5" r="2.2"/><path d="M5 16v-5a4 4 0 0 1 8 0v5M9 9v7"/></svg></span>
    <div><h3>Listen to Your Body</h3><p>You may feel relief, lightness, fatigue or even some tenderness. All of this can be normal.</p></div>
  </div>
  <div class="expect expect--support" style="left:233px;">
    <span class="badge"><svg width="18" height="18" viewBox="0 0 18 18" fill="none" stroke="#fff" stroke-width="1.1"><path d="M4.5 3h9l-1 12h-7Z"/><path d="M5 7h8"/></svg></span>
    <div><h3>Support Your Recovery</h3><p>Stay well hydrated, rest if needed and avoid overexertion so your body can heal and adapt.</p></div>
  </div>
  <div class="expect expect--trust" style="left:436px;">
    <span class="badge"><svg width="18" height="18" viewBox="0 0 18 18" fill="none" stroke="#fff" stroke-width="1.1"><circle cx="9" cy="9" r="6.5"/><path d="M9 5v4l2.5 2"/></svg></span>
    <div><h3>Trust the Process</h3><p>Healing is a journey, not a quick fix. Consistency and time create lasting change.</p></div>
  </div>

  <h2 class="section-title" style="left:30px;top:167px;"><span class="accent">Your</span> Recovery Journey</h2>
  <p class="lede" style="left:30px;top:194px;">Healing takes time, consistency and the right support. This is your roadmap. We’re with you every step of the way.</p>

  <div class="phase phase--relief">
    <h3>Phase 1: Relief Care</h3><p class="span">Weeks 1 - 6</p>
    <p>We focus on reducing pain and discomfort, calming your body and helping you begin to respond to treatment.</p>
  </div>
  <div class="phase phase--corrective">
    <h3>Phase 2: Corrective Care</h3><p class="span">Weeks 6 - 12</p>
    <p>We address the underlying issues, improve function and create more stable, lasting changes.</p>
  </div>
  <div class="phase phase--wellness">
    <h3>Phase 3: Wellness Care</h3><p class="span">Ongoing</p>
    <p>We help you maintain your progress, prevent relapse and support long-term health and wellbeing.</p>
  </div>
  <span class="connector" style="left:106px;"></span>
  <span class="connector" style="left:353px;"></span>
  <span class="connector" style="left:600px;"></span>

  <svg class="abs road" viewBox="0 340 706 120" aria-hidden="true">
    <defs>
      <linearGradient id="roadTone" x1="0" x2="706" y1="0" y2="0" gradientUnits="userSpaceOnUse">
        <stop offset="0" stop-color="#00a9dd"/>
        <stop offset="0.45" stop-color="#00bba5"/>
        <stop offset="0.75" stop-color="#3a97a8"/>
        <stop offset="1" stop-color="#8869af"/>
      </linearGradient>
    </defs>
    <path d="M-10,377 C40,387 70,432 104,432 S165,376 204,376 S265,432 304,432 S365,376 404,376 S465,432 504,432 S565,376 604,376 S665,420 716,425" fill="none" stroke="url(#roadTone)" stroke-width="26"/>
    <path d="M-10,377 C40,387 70,432 104,432 S165,376 204,376 S265,432 304,432 S365,376 404,376 S465,432 504,432 S565,376 604,376 S665,420 716,425" fill="none" stroke="#fff" stroke-width="1.2" stroke-dasharray="8 7"/>
  </svg>
  <div class="abs walker" role="img" aria-label="Small walking figure on the road"></div>

  <p class="promise" style="left:78px;"><svg width="15" height="15" viewBox="0 0 15 15" fill="none" stroke="#00ab8e" stroke-width="1.1"><circle cx="7.5" cy="7.5" r="6.5"/><path d="m4.5 7.6 2 2 4-4"/></svg>This is not a quick fix. It’s a journey.</p>
  <p class="promise" style="left:259px;"><svg width="15" height="15" viewBox="0 0 15 15" fill="none" stroke="#00ab8e" stroke-width="1.1"><circle cx="7.5" cy="7.5" r="6.5"/><path d="m4.5 7.6 2 2 4-4"/></svg>Progress takes time and consistency.</p>
  <p class="promise" style="left:448px;"><svg width="15" height="15" viewBox="0 0 15 15" fill="none" stroke="#00ab8e" stroke-width="1.1"><circle cx="7.5" cy="7.5" r="6.5"/><path d="m4.5 7.6 2 2 4-4"/></svg>Your care plan is individualised for you.</p>
</section>

</body>
</html>
```